Business Management Fortress

Assist with enhancing a powerpoint slide by providing a few design options for consideration. I have a template but open to any creative ideas.

Target Market(s)

Internal employees and stakeholders

Industry/Entity Type

Business Management, Finance, Accounting

Requirements
Must have
• Maintain a fortress, temple, or pyramid schema
Nice to have
• Scenic Background

```html
<!DOCTYPE html>
<html lang="en">
<head>
<meta charset="utf-8">
<title>Business Management Fortress</title>
<link href="https://fonts.googleapis.com/css2?family=Bebas+Neue&family=Lato:wght@400&display=swap" rel="stylesheet">
<style>
  :root {
    --bg-deep: #0a2a7a;
    --bg-mid: #1a4fb0;
    --bg-light: #3a78cc;
    --stone-light: #f2f2f2;
    --stone-mid: #cfcfcf;
    --stone-dark: #8e8e8e;
    --roof-edge: #7d7d7d;
    --roof-panel: #e3e3e3;
    --green: #6aa83a;
    --orange: #ef7f2a;
    --yellow: #f5c400;
    --red: #e00000;
    --white: #ffffff;
  }
  * { margin: 0; padding: 0; box-sizing: border-box; }
  html, body { width: 1200px; height: 675px; overflow: hidden; background: var(--bg-deep); }
  .slide { position: relative; width: 1200px; height: 675px; overflow: hidden; }
  .backdrop {
    position: absolute; inset: 0;
    background:
      radial-gradient(ellipse at 45% 30%, var(--bg-light) 0%, transparent 60%),
      linear-gradient(115deg, var(--bg-mid) 0%, var(--bg-deep) 75%);
  }
  .temple { position: absolute; left: 0; top: 0; width: 1200px; height: 675px; }
  .temple text { font-family: "Bebas Neue", sans-serif; fill: var(--white); }
  .temple .label-shadow { filter: drop-shadow(1px 1px 1px rgba(0,0,0,.45)); }
  .pillar-list { position: absolute; left: 817px; top: 122px; width: 380px; list-style: none; }
  .pillar-item { position: relative; height: 127px; padding-left: 76px; }
  .pillar-badge {
    position: absolute; left: 0; top: 0; width: 54px; height: 54px; border-radius: 50%;
    display: flex; align-items: center; justify-content: center;
  }
  .pillar-badge svg { width: 30px; height: 30px; }
  .pillar-title { font-family: "Bebas Neue", sans-serif; font-size: 17px; font-weight: 400; letter-spacing: .5px; color: var(--white); line-height: 1; margin-top: 8px; }
  .pillar-text { font-family: "Lato", sans-serif; font-size: 13px; line-height: 18px; color: var(--white); margin-top: 6px; white-space: nowrap; }
  .is-people { background: var(--green); }
  .is-innovation { background: var(--orange); }
  .is-intelligence { background: var(--yellow); }
  .is-alliances { background: var(--red); }
</style>
</head>
<body>
<div class="slide">
  <div class="backdrop" role="img" aria-label="Blue-toned view looking up at glass office towers"></div>

  <svg class="temple" viewBox="0 0 1280 720" aria-label="Temple diagram of business management">
    <defs>
      <linearGradient id="stone" x1="0" y1="0" x2="0" y2="1">
        <stop offset="0" stop-color="var(--stone-light)"/>
        <stop offset=".6" stop-color="var(--stone-mid)"/>
        <stop offset="1" stop-color="var(--stone-dark)"/>
      </linearGradient>
      <linearGradient id="stoneTop" x1="0" y1="0" x2="0" y2="1">
        <stop offset="0" stop-color="#bdbdbd"/>
        <stop offset="1" stop-color="#e8e8e8"/>
      </linearGradient>
      <linearGradient id="colGreen" x1="0" x2="1"><stop offset="0" stop-color="#3f7a1c"/><stop offset=".45" stop-color="#8fcf55"/><stop offset="1" stop-color="#3f7a1c"/></linearGradient>
      <linearGradient id="colOrange" x1="0" x2="1"><stop offset="0" stop-color="#b4500e"/><stop offset=".45" stop-color="#ffa04e"/><stop offset="1" stop-color="#b4500e"/></linearGradient>
      <linearGradient id="colYellow" x1="0" x2="1"><stop offset="0" stop-color="#b08a00"/><stop offset=".45" stop-color="#ffe24a"/><stop offset="1" stop-color="#b08a00"/></linearGradient>
      <linearGradient id="colRed" x1="0" x2="1"><stop offset="0" stop-color="#a00000"/><stop offset=".45" stop-color="#ff3a3a"/><stop offset="1" stop-color="#a00000"/></linearGradient>
    </defs>

    <!-- roof -->
    <polygon points="422,68 80,205 770,205" fill="var(--roof-edge)"/>
    <polygon points="422,84 280,135 422,192 564,135" fill="var(--roof-panel)"/>
    <polygon points="128,197 270,142 403,197" fill="var(--roof-panel)"/>
    <polygon points="441,197 574,142 718,197" fill="var(--roof-panel)"/>
    <g class="label-shadow">
      <text x="421" y="149" font-size="25" text-anchor="middle">PARTNER</text>
      <text x="254" y="189" font-size="25" text-anchor="middle">LEADER</text>
      <text x="580" y="189" font-size="25" text-anchor="middle">PROFITABILITY</text>
    </g>

    <!-- entablature -->
    <rect x="76" y="203" width="698" height="10" fill="#9a9a9a"/>
    <rect x="78" y="210" width="694" height="60" rx="8" fill="url(#stone)"/>

    <!-- platform -->
    <polygon points="30,590 820,590 822,600 28,600" fill="#9a9a9a"/>
    <rect x="28" y="598" width="794" height="54" rx="5" fill="url(#stone)"/>
    <polygon points="95,470 755,470 785,524 65,524" fill="url(#stoneTop)"/>
    <rect x="65" y="522" width="720" height="56" rx="5" fill="url(#stone)"/>
    <g class="label-shadow">
      <text x="412" y="561" font-size="27" text-anchor="middle">FIDUCIARY RESPONSIBILITIES</text>
      <text x="412" y="631" font-size="15" text-anchor="middle" letter-spacing=".5">ACCURATE FINANCIALS / INTERNAL CONTROLS / BRAND PROTECTION / COMPLIANCE / ETHICS / COST MANAGEMENT</text>
    </g>

    <!-- columns -->
    <g class="column">
      <rect x="122" y="270" width="72" height="198" fill="url(#colGreen)"/>
      <rect x="118" y="462" width="80" height="50" rx="10" fill="url(#colGreen)"/>
      <ellipse cx="158" cy="466" rx="40" ry="7" fill="#2f5e14" opacity=".6"/>
      <g fill="var(--white)">
        <circle cx="142" cy="318" r="3.5"/><rect x="138" y="323" width="8" height="20" rx="2"/>
        <circle cx="155" cy="318" r="3.5"/><rect x="151" y="323" width="8" height="20" rx="2"/>
        <circle cx="165" cy="332" r="2.5"/><rect x="162" y="336" width="6" height="10" rx="1.5"/>
      </g>
      <text transform="translate(161,409) rotate(-90)" font-size="18">PEOPLE</text>
    </g>
    <g class="column">
      <rect x="299" y="270" width="72" height="198" fill="url(#colOrange)"/>
      <rect x="295" y="462" width="80" height="50" rx="10" fill="url(#colOrange)"/>
      <ellipse cx="335" cy="466" rx="40" ry="7" fill="#8a3a06" opacity=".6"/>
      <g fill="var(--white)">
        <rect x="320" y="325" width="10" height="10"/><rect x="332" y="325" width="10" height="10"/>
        <rect x="320" y="337" width="10" height="10"/><rect x="332" y="337" width="10" height="10"/>
        <circle cx="343" cy="322" r="3"/>
      </g>
      <text transform="translate(340,438) rotate(-90)" font-size="18">INNOVATION</text>
    </g>
    <g class="column">
      <rect x="477" y="270" width="72" height="198" fill="url(#colYellow)"/>
      <rect x="473" y="462" width="80" height="50" rx="10" fill="url(#colYellow)"/>
      <ellipse cx="513" cy="466" rx="40" ry="7" fill="#7a6000" opacity=".6"/>
      <path d="M500 346 v-8 a14 14 0 1 1 22 -6 l4 6 h-4 v6 h-8 v4 z" fill="var(--white)"/>
      <circle cx="511" cy="328" r="4" fill="var(--yellow)"/>
      <text transform="translate(518,446) rotate(-90)" font-size="18">INTELLIGENCE</text>
    </g>
    <g class="column">
      <rect x="654" y="270" width="72" height="198" fill="url(#colRed)"/>
      <rect x="650" y="462" width="80" height="50" rx="10" fill="url(#colRed)"/>
      <ellipse cx="690" cy="466" rx="40" ry="7" fill="#700000" opacity=".6"/>
      <rect x="677" y="318" width="24" height="24" rx="2" fill="none" stroke="var(--white)" stroke-width="2.5"/>
      <path d="M682 324 l4 4 m0 -4 l-4 4 M691 332 l4 4 m0 -4 l-4 4 M684 337 q6 -2 8 -12" stroke="var(--white)" stroke-width="1.6" fill="none"/>
      <text transform="translate(685,428) rotate(-90)" font-size="17">STRATEGIC</text>
      <text transform="translate(700,428) rotate(-90)" font-size="17">ALLIANCES</text>
    </g>
  </svg>

  <ul class="pillar-list">
    <li class="pillar-item">
      <span class="pillar-badge is-people"><svg viewBox="0 0 30 30" fill="#fff"><circle cx="9" cy="6" r="3"/><rect x="6" y="10" width="6" height="15" rx="2"/><circle cx="18" cy="6" r="3"/><rect x="15" y="10" width="6" height="15" rx="2"/><circle cx="25" cy="16" r="2"/><rect x="23" y="19" width="4" height="7" rx="1"/></svg></span>
      <h3 class="pillar-title">PEOPLE</h3>
      <p class="pillar-text">Lorem ipsum dolor sit amet,<br>consectetuer adipiscing elit. Maecenas<br>porttitor congue massa. Fusce posuere,<br>magna sed pulvinar ultricies, purus</p>
    </li>
    <li class="pillar-item">
      <span class="pillar-badge is-innovation"><svg viewBox="0 0 30 30" fill="#fff"><rect x="5" y="9" width="9" height="9"/><rect x="16" y="9" width="9" height="9"/><rect x="5" y="20" width="9" height="9"/><rect x="16" y="20" width="9" height="9"/><circle cx="24" cy="5" r="3"/></svg></span>
      <h3 class="pillar-title">INNOVATION</h3>
      <p class="pillar-text">Lorem ipsum dolor sit amet,<br>consectetuer adipiscing elit. Maecenas<br>porttitor congue massa. Fusce posuere,<br>magna sed pulvinar ultricies, purus</p>
    </li>
    <li class="pillar-item">
      <span class="pillar-badge is-intelligence"><svg viewBox="0 0 30 30"><path d="M7 28 v-9 a10 10 0 1 1 17 -6 l3 5 h-3 v5 h-6 v5 z" fill="#fff"/><circle cx="14" cy="12" r="3.5" fill="#f5c400"/></svg></span>
      <h3 class="pillar-title">INTELLIGENCE</h3>
      <p class="pillar-text">Lorem ipsum dolor sit amet,<br>consectetuer adipiscing elit. Maecenas<br>porttitor congue massa. Fusce posuere,<br>magna sed pulvinar ultricies, purus</p>
    </li>
    <li class="pillar-item">
      <span class="pillar-badge is-alliances"><svg viewBox="0 0 30 30" fill="none" stroke="#fff"><rect x="4" y="4" width="22" height="22" rx="2" stroke-width="2.5"/><path d="M8 9 l4 4 m0 -4 l-4 4 M18 18 l4 4 m0 -4 l-4 4 M10 22 q6 -2 8 -12" stroke-width="1.6"/></svg></span>
      <h3 class="pillar-title">STRATEGIC ALLIANCES</h3>
      <p class="pillar-text">Lorem ipsum dolor sit amet,<br>consectetuer adipiscing elit. Maecenas<br>porttitor congue massa. Fusce posuere,<br>magna sed pulvinar ultricies, purus</p>
    </li>
  </ul>
</div>
</body>
</html>
```